Kelvane Plumbing Business cards

Company is Kelvane Plumbing.
name Dashel Morrowby, I am a plumber, drainer, gasfitter and roofer
Mobile: 0431 906 154
Email address: info@kelvaneplumbing.example (check out my website for some ideas)
Website: www.kelvaneplumbing.example
ABN: 82 916 203 471
LIC: 604517K

I am reliable all round plumber. I am a 24 hour emergency service. Kelvane Plumbing is a professional plumbing service in the Illawarra, South Coast, Southern Sydney and Southern Highland regions of NSW. We offer a 24 hour emergency service for piece of mind to our customers. Call us now to see how we can help you. Kelvane Plumbing approaches every job with attention to detail and excellent customer service. With our superior workmanship you can be confident that the job will be done right the first time around. You can rest assured with results that are guaranteed to last.

Target Market(s)

the general public

Contact Information for Business Card

look up website for some ideas something with similar colours to logo and new modern and to catch the eye.

Colors
fdfdfd
ffffff
000000
7f7f7f
aaaaaa
33a6d7
0492cd

Requirements
Must have
• all contact details
• company- Kelvane Plumbing
• name- Dashel Morrowby
• number mobile- 0431 906 154
• Email address- info@kelvaneplumbing.example
• Website- www.kelvaneplumbing.example
• ABN- 82 916 203 471
• LIC- 604517K

```html
<!DOCTYPE html>
<html lang="en">
<head>
<meta charset="utf-8">
<title>Kelvane Plumbing – Business Cards</title>
<link href="https://fonts.googleapis.com/css2?family=Roboto:wght@300;400;500;700&display=swap" rel="stylesheet">
<style>
  :root {
    --bg: #2a3340;
    --card-dark: #1b1b1c;
    --card-light: #ffffff;
    --ink-dark: #000000;
    --ink-light: #fdfdfd;
    --grey: #7f7f7f;
    --grey-soft: #aaaaaa;
    --blue: #0492cd;
    --blue-light: #33a6d7;
  }
  * { margin: 0; padding: 0; box-sizing: border-box; }
  html, body { width: 1200px; height: 1200px; overflow: hidden; }
  body {
    background: var(--bg);
    font-family: "Roboto", Arial, sans-serif;
    position: relative;
  }
  .card {
    position: absolute;
    width: 540px;
    height: 309px;
    overflow: hidden;
    box-shadow: 0 10px 30px rgba(0,0,0,0.35);
  }
  .card--back { left: 330px; top: 220px; background: var(--card-dark); }
  .card--front-dark { left: 40px; top: 640px; background: var(--card-dark); }
  .card--front-light { left: 620px; top: 640px; background: var(--card-light); }

  /* back */
  .back-brand {
    position: absolute; left: 0; right: 0; top: 92px;
    text-align: center;
  }
  .back-brand .brand-name {
    font-weight: 700; font-size: 34px; letter-spacing: 1px;
    color: var(--blue); text-transform: uppercase; line-height: 1.05;
  }
  .back-brand .brand-name span { display: block; font-size: 18px; letter-spacing: 9px; }
  .website {
    position: absolute; left: 0; right: 0; bottom: 56px;
    text-align: center; color: var(--ink-light);
    font-weight: 300; font-size: 16px; letter-spacing: 6px;
  }

  /* front */
  .ghost {
    position: absolute; left: -30px; top: 40px;
    width: 260px; height: 260px;
  }
  .ghost-text {
    position: absolute; left: -10px; top: 135px;
    font-weight: 700; font-size: 38px; text-transform: uppercase;
    letter-spacing: 1px;
  }
  .card--front-dark .ghost-text { color: rgba(255,255,255,0.05); }
  .card--front-light .ghost-text { color: rgba(0,0,0,0.07); }

  .front-brand {
    position: absolute; right: 36px; top: 40px; text-align: right;
    font-weight: 700; font-size: 28px; text-transform: uppercase; line-height: 1.05;
    letter-spacing: 1px;
  }
  .front-brand span { display: block; font-size: 14px; letter-spacing: 8px; }
  .card--front-dark .front-brand { color: var(--ink-light); }
  .card--front-light .front-brand { color: var(--ink-dark); }

  .contact {
    position: absolute; left: 282px; top: 178px;
    font-size: 13px; line-height: 1.45;
  }
  .contact strong { font-weight: 700; letter-spacing: 1.5px; font-size: 14px; }
  .card--front-dark .contact { color: var(--ink-light); }
  .card--front-light .contact { color: var(--ink-dark); }

  .person { position: absolute; left: 30px; bottom: 34px; }
  .person-name {
    color: var(--blue); font-weight: 500; font-size: 24px;
    text-transform: uppercase; letter-spacing: 0.2px;
  }
  .person-role { font-size: 12px; font-weight: 300; margin-top: 2px; }
  .card--front-dark .person-role { color: var(--grey); }
  .card--front-light .person-role { color: var(--grey); }
</style>
</head>
<body>

  <section class="card card--back" aria-label="Card back">
    <div class="back-brand">
      <div class="brand-name">Kelvane<span>Plumbing</span></div>
    </div>
    <p class="website">www.kelvaneplumbing.example</p>
  </section>

  <section class="card card--front-dark" aria-label="Card front, dark">
    <svg class="ghost" viewBox="0 0 260 260" aria-hidden="true">
      <circle cx="130" cy="130" r="115" fill="none" stroke="rgba(255,255,255,0.04)" stroke-width="16"/>
    </svg>
    <div class="ghost-text" aria-hidden="true">Kelvane</div>
    <div class="front-brand">Kelvane<span>Plumbing</span></div>
    <div class="contact">
      Mobile: <strong>0431 906 154</strong><br>
      Email: info@kelvaneplumbing.example<br>
      LIC: 604517K<br>
      ABN: 82 916 203 471
    </div>
    <div class="person">
      <div class="person-name">Dashel Morrowby</div>
      <div class="person-role">I am a plumber, drainer, gasfitter and roofer</div>
    </div>
  </section>

  <section class="card card--front-light" aria-label="Card front, light">
    <svg class="ghost" viewBox="0 0 260 260" aria-hidden="true">
      <circle cx="130" cy="130" r="115" fill="none" stroke="rgba(0,0,0,0.06)" stroke-width="16"/>
    </svg>
    <div class="ghost-text" aria-hidden="true">Kelvane</div>
    <div class="front-brand">Kelvane<span>Plumbing</span></div>
    <div class="contact">
      Mobile: <strong>0431 906 154</strong><br>
      Email: info@kelvaneplumbing.example<br>
      LIC: 604517K<br>
      ABN: 82 916 203 471
    </div>
    <div class="person">
      <div class="person-name">Dashel Morrowby</div>
      <div class="person-role">I am a plumber, drainer, gasfitter and roofer</div>
    </div>
  </section>

</body>
</html>
```